BRTW Traditional Business Card Project

Please see attached....just a simple business card... on attachment- please use the exact font, style, etc as the attached "Dal Rupert Huxley" card... however, replace with the "Owen Bartholomew Lindqvist" text and address below the card.

```html
<!DOCTYPE html>
<html lang="en">
<head>
<meta charset="utf-8">
<title>BRTW Business Card</title>
<link rel="stylesheet" href="https://fonts.googleapis.com/css2?family=Cinzel:wght@400;700&family=Questrial&display=swap">
<style>
  :root {
    --page-bg: #e9ebea;
    --card-frame: #7b7b7b;
    --card-face: #d4d9d7;
    --corner-mark: #f6f7f7;
    --ink: #111111;
    --ink-soft: #2a2a2a;
  }
  html, body {
    margin: 0;
    padding: 0;
    width: 1200px;
    height: 900px;
    overflow: hidden;
    background: var(--page-bg);
  }
  .canvas {
    position: relative;
    width: 1200px;
    height: 900px;
  }
  .card {
    position: absolute;
    left: 75px;
    top: 150px;
    width: 1050px;
    height: 600px;
    box-sizing: border-box;
    background: var(--card-frame);
    padding: 24px;
  }
  .card-face {
    position: relative;
    width: 100%;
    height: 100%;
    background: var(--card-face);
    color: var(--ink);
  }
  .corner-marks {
    position: absolute;
    inset: 0;
    width: 100%;
    height: 100%;
  }
  .firm {
    position: absolute;
    left: 38px;
    top: 30px;
    font-family: "Cinzel", serif;
  }
  .firm-name {
    font-weight: 700;
    font-size: 46px;
    letter-spacing: 0.02em;
    line-height: 1;
  }
  .firm-suffix {
    font-family: "Questrial", sans-serif;
    font-size: 16px;
    letter-spacing: 0.28em;
    text-transform: uppercase;
    margin-top: 8px;
    margin-left: 18px;
    color: var(--ink-soft);
  }
  .attorney {
    position: absolute;
    left: 0;
    right: 0;
    top: 208px;
    text-align: center;
    font-family: "Cinzel", serif;
  }
  .attorney-name {
    font-weight: 700;
    font-size: 46px;
    letter-spacing: 0.02em;
    line-height: 1;
  }
  .attorney-title {
    font-family: "Questrial", sans-serif;
    font-size: 18px;
    letter-spacing: 0.55em;
    text-transform: uppercase;
    margin-top: 6px;
    padding-left: 300px;
    color: var(--ink-soft);
  }
  .contact {
    position: absolute;
    right: 60px;
    top: 340px;
    font-family: "Questrial", sans-serif;
    font-size: 23px;
    line-height: 1.4;
    letter-spacing: 0.06em;
  }
  .address {
    position: absolute;
    left: 48px;
    bottom: 36px;
    font-family: "Questrial", sans-serif;
    font-size: 23px;
    line-height: 1.4;
    letter-spacing: 0.08em;
  }
  .upper { text-transform: uppercase; }
</style>
</head>
<body>
<main class="canvas">
  <section class="card">
    <div class="card-face">
      <svg class="corner-marks" viewBox="0 0 1002 552" preserveAspectRatio="none" aria-hidden="true">
        <g fill="var(--corner-mark)">
          <path d="M0 0 H78 V9 H9 V78 H0 Z"/>
          <path d="M1002 0 H924 V9 H993 V78 H1002 Z"/>
          <path d="M0 552 H78 V543 H9 V474 H0 Z"/>
          <path d="M1002 552 H924 V543 H993 V474 H1002 Z"/>
        </g>
      </svg>

      <header class="firm">
        <div class="firm-name">Bramble Ridge</div>
        <div class="firm-suffix">Trial Workers, PLC</div>
      </header>

      <div class="attorney">
        <div class="attorney-name">Owen Bartholomew Lindqvist</div>
        <div class="attorney-title">Attorney at Law</div>
      </div>

      <div class="contact">
        <div class="upper">Tel (555) 214-0187</div>
        <div class="upper">Fax (555) 214-0190</div>
        <div>olindqvist@lawbrtw.com</div>
      </div>

      <address class="address" style="font-style: normal;">
        <div class="upper">1420 Alder Court, Suite B</div>
        <div class="upper">Fernvale Heights, CA 91000</div>
        <div>www.lawbrtw.com</div>
      </address>
    </div>
  </section>
</main>
</body>
</html>
```